Need help in designing new business card utilizing our new logo.

BuildMarq Solutions works with Construction Business Owners, Managers & IT Professionals to strengthen software usage and increase user productivity.

Our Construction Accounting and Mobile Field Management Software Clients engage with us in the following areas:

New Software Implementations
Software Re-Implementations
Redesigning Software Usage at the User Level
Project Coordination & Management
Continued Software Support

Old tag line:
Planning Smarter - Building Better Systems

www.buildmarq-solutions.example

Stride 4 is a product, but not needed for a new business card.

```html
<!DOCTYPE html>
<html lang="en">
<head>
<meta charset="utf-8">
<title>BuildMarq Solutions – Business Card</title>
<link href="https://fonts.googleapis.com/css2?family=Jost:wght@400;500;600&family=Oswald:wght@500&display=swap" rel="stylesheet">
<style>
  :root {
    --backdrop: #2b2b2b;
    --card: #1d1d1e;
    --ink-white: #f2f2f2;
    --ink-soft: #cfcfcf;
    --ink-grey: #9a9a9a;
    --accent: #3a3fb8;
  }
  * { margin: 0; padding: 0; box-sizing: border-box; }
  html, body { width: 1200px; height: 899px; overflow: hidden; }
  body {
    background: var(--backdrop);
    font-family: "Jost", sans-serif;
    display: flex;
    flex-direction: column;
    align-items: center;
    justify-content: center;
    gap: 40px;
  }
  .card {
    position: relative;
    width: 700px;
    height: 400px;
    background: var(--card);
    box-shadow: 0 10px 30px rgba(0,0,0,.45);
  }

  /* Front */
  .front-brand {
    position: absolute;
    left: 0; right: 0; top: 130px;
    display: flex;
    justify-content: center;
    align-items: center;
    gap: 18px;
  }
  .brand-square { width: 30px; height: 30px; flex: none; }
  .front-brand .brand-square { background: var(--ink-grey); }
  .brand-name {
    font-family: "Jost", sans-serif;
    font-weight: 500;
    font-size: 40px;
    letter-spacing: 2px;
    text-transform: uppercase;
    line-height: 1;
    white-space: nowrap;
  }
  .front-brand .brand-name { color: var(--ink-grey); }
  .tagline {
    position: absolute;
    left: 0; right: 0; bottom: 52px;
    text-align: center;
    color: var(--ink-soft);
    font-size: 17px;
    letter-spacing: 1.2px;
  }

  /* Back */
  .holder { position: absolute; left: 44px; top: 38px; }
  .holder-name {
    font-family: "Oswald", sans-serif;
    font-weight: 500;
    font-size: 40px;
    color: var(--ink-white);
    text-transform: uppercase;
    line-height: 1.05;
  }
  .holder-role { font-size: 20px; font-weight: 600; color: var(--ink-white); }

  .back-brand {
    position: absolute;
    right: 40px; top: 150px;
    display: flex;
    align-items: center;
    gap: 12px;
  }
  .back-brand .brand-square { background: var(--accent); width: 22px; height: 22px; }
  .back-brand .brand-name { color: var(--accent); font-size: 26px; }

  .contact-list {
    position: absolute; left: 44px; bottom: 44px;
    list-style: none;
    color: var(--ink-white);
    font-size: 16px;
    line-height: 27px;
    letter-spacing: .3px;
  }
  .contact-list li { display: flex; align-items: center; gap: 12px; white-space: nowrap; }
  .contact-list svg { width: 16px; height: 16px; fill: none; stroke: var(--accent); stroke-width: 2; flex: none; }
  .contact-list svg .solid { fill: var(--accent); stroke: none; }

  .address {
    position: absolute; right: 40px; bottom: 40px;
    text-align: right;
    color: var(--ink-white);
    font-size: 16px;
    font-style: normal;
    line-height: 27px;
    letter-spacing: .5px;
  }
</style>
</head>
<body>

  <section class="card card-front">
    <div class="front-brand">
      <span class="brand-square"></span>
      <span class="brand-name">BuildMarq Solutions</span>
    </div>
    <p class="tagline">Planning Smarter - Building Better Systems</p>
  </section>

  <section class="card card-back">
    <div class="holder">
      <h1 class="holder-name">Dana R. Whitfield</h1>
      <p class="holder-role">Owner</p>
    </div>

    <div class="back-brand">
      <span class="brand-square"></span>
      <span class="brand-name">BuildMarq Solutions</span>
    </div>

    <ul class="contact-list">
      <li>
        <svg viewBox="0 0 16 16" aria-hidden="true"><path d="M3 2l3 0 1 3-2 1.5a8 8 0 0 0 4.5 4.5L11 9l3 1v3a1 1 0 0 1-1 1A12 12 0 0 1 2 3a1 1 0 0 1 1-1z"/></svg>
        866-555-0142 ext.100
      </li>
      <li>
        <svg viewBox="0 0 16 16" aria-hidden="true"><rect x="4" y="1.5" width="8" height="13" rx="1.5"/><circle class="solid" cx="8" cy="12" r="1"/></svg>
        518-555-0187
      </li>
      <li>
        <svg viewBox="0 0 16 16" aria-hidden="true"><rect class="solid" x="1" y="3" width="14" height="10" rx="1"/><path d="M1.5 4l6.5 5 6.5-5" stroke="#1d1d1e"/></svg>
        dana.whitfield@buildmarq-solutions.example
      </li>
      <li>
        <svg viewBox="0 0 16 16" aria-hidden="true"><circle cx="9.5" cy="6.5" r="4.5"/><path d="M6.3 9.7L1.5 14.5"/></svg>
        www.buildmarq-solutions.example
      </li>
    </ul>

    <address class="address">
      48 Linden Avenue - PMB 117<br>
      Maple Ridge NY 12000
    </address>
  </section>

</body>
</html>
```